BRICKVALE Norvik Paltera 2022 Vehicle Wrap

For Design Inspiration; Please visit www.brickvaleinspections.com
We are in need of a full vehicle wrap for a Norvik Paltera 2022.  All design submissions must be designed to this vehicle body. Any designs shown on other vehicles will not be accepted.  Please read the following design brief for guidance.
Company Information:
BRICKVALE Inspections
Located in United States Florida
Home Inspection Company.
Brand Identity:  Our brand's logo is influenced by a technical theme such as an architectural building plan set / blueprint.  We have two versions of our Logo.  "BRICKVALE" when designing including the "home inspections" bottom portion of the logo is optional.   We serve our local community by providing home inspections on brand new construction homes and specialize in performing inspections in the luxury market.  The design should be clean,  easy to understand and eye catching.  Remember when a vehicle is driving down the road you have little time to read any small text.  We have provided a visual example of a sample design we like and examples of bad design.
Design Brief Details
NOTES
Avoid excessive wording on design.
We want to communicate, who we are.
Must Include:
www.brickvaleinspections.com
512-608-2931
LOGO
Possible Tag Lines
CERTIFIED. EXPERIENCED. TRUSTED.
EVERY DETAIL OF YOUR HOME

Updates
Low design quality
Target Market(s)
Home Buyers
Industry/Entity Type
Real Estate
Colors
Designer to choose colors to be used in the design.
Requirements
Should not have
- bullet points, social media tags, qr codes or small text

```html
<!DOCTYPE html>
<html lang="en">
<head>
<meta charset="utf-8">
<title>BRICKVALE Inspections – Norvik Paltera Wrap Concepts</title>
<link rel="stylesheet" href="https://fonts.googleapis.com/css2?family=Montserrat:wght@500;700;800&family=Poppins:wght@500;600;700&display=swap">
<style>
  :root {
    --wrap-white: #f4f4f2;
    --brand-green: #4caf2e;
    --ink: #2b2b2b;
    --rear-dark: #2a2724;
    --rear-charcoal: #2e2e2e;
    --canvas: #ffffff;
    --text-light: #ffffff;
  }
  html, body {
    margin: 0;
    width: 1200px;
    height: 1200px;
    overflow: hidden;
    background: var(--canvas);
  }
  .wrap-sheet {
    width: 1200px;
    height: 1200px;
    box-sizing: border-box;
    padding: 90px 80px;
    display: flex;
    flex-direction: column;
    justify-content: space-between;
  }
  .wrap-variant {
    display: block;
    width: 1040px;
    height: 280px;
  }
  .body-panel { fill: var(--wrap-white); }
  .brand-name { font-family: "Montserrat", sans-serif; font-weight: 800; font-size: 78px; fill: var(--ink); letter-spacing: 1px; }
  .brand-rule { fill: var(--brand-green); }
  .brand-sub { font-family: "Montserrat", sans-serif; font-weight: 500; font-size: 25px; letter-spacing: 9px; fill: var(--ink); }
  .tagline-band { fill: var(--brand-green); }
  .tagline-text { font-family: "Poppins", sans-serif; font-weight: 600; font-size: 21px; fill: var(--text-light); }
  .accent-green { fill: var(--brand-green); }
  .accent-white { fill: var(--wrap-white); }
  .rear-dark { fill: var(--rear-dark); }
  .rear-charcoal { fill: var(--rear-charcoal); }
  .phone { font-family: "Poppins", sans-serif; font-weight: 600; font-size: 36px; fill: var(--text-light); letter-spacing: 2px; }
  .web { font-family: "Poppins", sans-serif; font-weight: 600; font-size: 16px; fill: var(--text-light); }
  .promise { font-family: "Poppins", sans-serif; font-weight: 700; font-size: 14px; letter-spacing: 1px; }
  .promise-green { fill: var(--brand-green); }
  .promise-white { fill: var(--text-light); }
  .promise-dark { fill: var(--ink); }
</style>
</head>
<body>
<main class="wrap-sheet">

  <!-- Concept one: dark rear with green stripe, green promise -->
  <svg class="wrap-variant" viewBox="0 0 1040 280" aria-label="Wrap concept one">
    <rect class="body-panel" x="0" y="0" width="1040" height="280" rx="24"/>
    <path class="rear-dark" d="M680 0 H1016 Q1040 0 1040 24 V256 Q1040 280 1016 280 H600 Z"/>
    <polygon class="accent-green" points="610,20 668,20 588,260 530,260"/>
    <polygon class="accent-green" points="690,0 720,0 600,280 570,280"/>
    <text class="brand-name" x="70" y="120">BRICKVALE</text>
    <rect class="brand-rule" x="70" y="138" width="470" height="5"/>
    <text class="brand-sub" x="72" y="180">HOME INSPECTIONS</text>
    <polygon class="tagline-band" points="30,198 560,198 545,234 30,234"/>
    <text class="tagline-text" x="80" y="224">EVERY DETAIL OF YOUR HOME</text>
    <text class="phone" x="745" y="60">512-608-2931</text>
    <text class="web" x="745" y="90">www.brickvaleinspections.com</text>
    <text class="promise promise-green" x="905" y="190">CERTIFIED.</text>
    <text class="promise promise-green" x="905" y="208">EXPERIENCED.</text>
    <text class="promise promise-green" x="905" y="226">TRUSTED.</text>
  </svg>

  <!-- Concept two: charcoal rear, white promise -->
  <svg class="wrap-variant" viewBox="0 0 1040 280" aria-label="Wrap concept two">
    <rect class="body-panel" x="0" y="0" width="1040" height="280" rx="24"/>
    <path class="rear-charcoal" d="M680 0 H1016 Q1040 0 1040 24 V256 Q1040 280 1016 280 H600 Z"/>
    <polygon class="accent-green" points="610,20 668,20 588,260 530,260"/>
    <polygon class="accent-white" points="672,0 690,0 610,280 592,280"/>
    <text class="brand-name" x="70" y="120">BRICKVALE</text>
    <rect class="brand-rule" x="70" y="138" width="470" height="5"/>
    <text class="brand-sub" x="72" y="180">HOME INSPECTIONS</text>
    <polygon class="tagline-band" points="30,198 560,198 545,234 30,234"/>
    <text class="tagline-text" x="80" y="224">EVERY DETAIL OF YOUR HOME</text>
    <text class="phone" x="745" y="60">512-608-2931</text>
    <text class="web" x="745" y="90">www.brickvaleinspections.com</text>
    <text class="promise promise-white" x="880" y="190">CERTIFIED.</text>
    <text class="promise promise-white" x="880" y="208">EXPERIENCED.</text>
    <text class="promise promise-white" x="880" y="226">TRUSTED.</text>
  </svg>

  <!-- Concept three: dark rear with green lower sweep -->
  <svg class="wrap-variant" viewBox="0 0 1040 280" aria-label="Wrap concept three">
    <rect class="body-panel" x="0" y="0" width="1040" height="280" rx="24"/>
    <path class="rear-charcoal" d="M640 0 H1016 Q1040 0 1040 24 V256 Q1040 280 1016 280 H540 Z"/>
    <polygon class="accent-green" points="620,0 650,0 550,280 520,280"/>
    <path class="accent-green" d="M650 232 L1040 176 V246 Q1040 266 1020 266 H640 Z"/>
    <text class="brand-name" x="70" y="120">BRICKVALE</text>
    <rect class="brand-rule" x="70" y="138" width="470" height="5"/>
    <text class="brand-sub" x="72" y="180">HOME INSPECTIONS</text>
    <polygon class="tagline-band" points="30,198 560,198 545,234 30,234"/>
    <text class="tagline-text" x="80" y="224">EVERY DETAIL OF YOUR HOME</text>
    <text class="phone" x="690" y="60">512-608-2931</text>
    <text class="web" x="700" y="90">www.brickvaleinspections.com</text>
    <text class="promise promise-dark" x="905" y="212">CERTIFIED.</text>
    <text class="promise promise-dark" x="905" y="230">EXPERIENCED.</text>
    <text class="promise promise-dark" x="905" y="248">TRUSTED.</text>
  </svg>

</main>
</body>
</html>
```